New Business Card Design Project

I have a logo I would like to use on the business card. I want something that will stand out and that will be remembered.

Target Market(s)

People who collect gems, minerals and crystals.

Contact Information for Business Card

email - mkthestonefalcon@vendrollo.com
phone # 917-406-2581

Font styles to use
Serif
Sans Serif
Decorative

Colors

Designer to choose colors to be used in the design.

Requirements
Must have
• The logo...two to choose from.
Nice to have
• An eye catching and memorable way to draw in people who collect gems minerals and crystals.

```html
<!DOCTYPE html>
<html lang="en">
<head>
<meta charset="utf-8">
<title>The Stone Falcon – Business Card</title>
<link href="https://fonts.googleapis.com/css2?family=Open+Sans:wght@400;600;700&display=swap" rel="stylesheet">
<style>
  :root {
    --backdrop: #e9e6e1;
    --kraft: #cdb896;
    --kraft-light: #d6c3a3;
    --ink: #9a8564;
    --ink-dark: #8a7556;
    --lilac: #9a80d6;
    --groove-dark: rgba(110, 90, 60, 0.45);
    --groove-light: rgba(255, 248, 232, 0.55);
  }
  * { margin: 0; padding: 0; box-sizing: border-box; }
  html, body {
    width: 1200px; height: 900px; overflow: hidden;
    background: var(--backdrop);
    font-family: "Open Sans", Arial, sans-serif;
  }
  .canvas {
    width: 1200px; height: 900px;
    display: flex; align-items: center; justify-content: center;
  }
  .card {
    position: relative;
    width: 1000px; height: 572px;
    border-radius: 28px;
    background: radial-gradient(ellipse at 35% 30%, var(--kraft-light), var(--kraft) 70%);
    box-shadow: 0 10px 30px rgba(60, 45, 25, 0.25);
    display: flex;
    overflow: hidden;
  }
  .emboss {
    color: var(--ink);
    text-shadow: -1px -1px 0 rgba(90, 70, 40, 0.35), 1px 1px 0 var(--groove-light);
  }
  .brand-panel {
    width: 50%;
    display: flex; flex-direction: column; align-items: center; justify-content: center;
    gap: 22px;
  }
  .brand-mark {
    width: 120px; height: 120px; border-radius: 50%;
    background: var(--kraft);
    box-shadow: inset 2px 2px 3px var(--groove-dark), inset -2px -2px 3px var(--groove-light);
  }
  .brand-name {
    font-weight: 700; font-size: 44px; letter-spacing: 3px;
    text-transform: uppercase; text-align: center; line-height: 1.1;
  }
  .divider {
    width: 4px; margin: 70px 0;
    border-left: 2px solid var(--groove-dark);
    border-right: 2px solid var(--groove-light);
  }
  .contact-panel {
    flex: 1;
    display: flex; flex-direction: column; align-items: center; justify-content: center;
    text-align: center;
  }
  .person-name {
    font-size: 40px; font-weight: 400; letter-spacing: 2px; text-transform: uppercase;
  }
  .person-name .surname { color: var(--lilac); font-weight: 600; text-shadow: none; }
  .person-role {
    font-size: 21px; letter-spacing: 2px; text-transform: uppercase; margin-top: 2px;
  }
  .contact-icons { display: flex; gap: 18px; margin: 28px 0 18px; }
  .contact-icons svg { width: 44px; height: 44px; }
  .contact-line { font-size: 30px; line-height: 1.35; }
  .contact-email { font-size: 27px; }
</style>
</head>
<body>
<main class="canvas">
  <article class="card">
    <section class="brand-panel">
      <div class="brand-mark"></div>
      <div class="brand-name emboss">The Stone<br>Falcon</div>
    </section>
    <div class="divider"></div>
    <section class="contact-panel">
      <h1 class="person-name emboss">Marcus <span class="surname">Kell</span></h1>
      <p class="person-role emboss">CEO/Owner</p>
      <div class="contact-icons">
        <svg viewBox="0 0 44 44" aria-label="Phone">
          <circle cx="22" cy="22" r="19" fill="none" stroke="var(--lilac)" stroke-width="3"/>
          <path d="M16 13c2 0 3 4 2 5l-2 2c1 3 3 5 6 6l2-2c1-1 5 0 5 2l-1 3c-1 1-3 1-5 0-5-2-9-6-11-11-1-2-1-4 0-5z" fill="none" stroke="var(--lilac)" stroke-width="2.2" stroke-linejoin="round"/>
        </svg>
        <svg viewBox="0 0 44 44" aria-label="Email">
          <circle cx="22" cy="22" r="19" fill="none" stroke="var(--lilac)" stroke-width="3"/>
          <rect x="12" y="15" width="20" height="14" fill="none" stroke="var(--lilac)" stroke-width="2.2"/>
          <path d="M12 15l10 8 10-8" fill="none" stroke="var(--lilac)" stroke-width="2.2"/>
        </svg>
      </div>
      <p class="contact-line emboss">917-406-2581</p>
      <p class="contact-line contact-email emboss">mkthestonefalcon@vendrollo.com</p>
    </section>
  </article>
</main>
</body>
</html>
```